Redesign website

I purchased a business a few months ago and I'm in the process on rebranding everything and creating a new website. I want the new website completely different with 5 pages and nice pictures on every page. Also I want my new logo and colors to included on the site.
Current Site https://www.brindlehoundco.com

Industry/Entity Type

Dog Sitting

Coding

Coded - Design and coding required

Number of Pages Required

5+ page

Requirements
Must have
• I have pictures and a video I can shared to use for the website.
Just as the current site it should have an option to be taken to the site I have to make reservations.
Nice to have
• Would be nice to have social media intergrations

```html
<!DOCTYPE html>
<html lang="en">
<head>
<meta charset="utf-8">
<title>Brindle Hound – Pet Boarding & Daycare</title>
<link href="https://fonts.googleapis.com/css2?family=Playfair+Display:wght@400;700&family=Raleway:wght@300;400&family=Montserrat:wght@600;700&display=swap" rel="stylesheet">
<style>
:root{
  --teal:#1cb5c4;
  --teal-band:#00b4c5;
  --magenta:#c4168f;
  --bubble-teal:#82d8e0;
  --bubble-pink:#e07cc4;
  --ink:#2b2b2b;
  --muted:#8a8a8a;
  --grey-top:#e6e6e6;
  --grey-bottom:#efefef;
  --footer:#333333;
  --white:#ffffff;
}
*{box-sizing:border-box;margin:0;padding:0}
html,body{width:1200px;height:3670px;overflow:hidden;background:var(--white)}
body{position:relative;font-family:"Raleway",sans-serif;color:var(--ink)}
.abs{position:absolute}
.serif{font-family:"Playfair Display",serif}

/* header */
.brand{left:0;width:1200px;top:22px;text-align:center;display:flex;justify-content:center;align-items:center;gap:12px}
.brand-dot{width:22px;height:22px;border-radius:50%;background:var(--magenta)}
.brand-name{font-family:"Playfair Display",serif;font-weight:700;font-size:40px;color:var(--teal)}
.nav{left:100px;width:1000px;top:130px;height:52px;border-top:1px solid #e4e4e4;border-bottom:1px solid #e4e4e4;display:flex;justify-content:center;align-items:center;gap:36px}
.nav a,.footer-nav a{font-family:"Playfair Display",serif;font-size:15px;letter-spacing:2px;text-transform:uppercase;color:#777;text-decoration:none}
.nav a.active,.footer-nav a.active{color:var(--teal)}

/* hero */
.hero{left:0;top:205px;width:1200px;height:533px;background:linear-gradient(100deg,#3e4a2a 0%,#5c5a34 35%,#7a5a3c 55%,#b8553f 75%,#4a3a2a 100%)}
.hero-copy{left:152px;top:60px;color:var(--white)}
.hero-copy .big{font-family:"Playfair Display",serif;font-weight:700;font-size:66px;line-height:72px}
.hero-copy .accent{font-family:"Playfair Display",serif;font-size:44px;color:var(--teal);line-height:60px}
.hero-copy .mid{font-family:"Playfair Display",serif;font-size:44px;line-height:46px}
.btn-solid{display:flex;align-items:center;justify-content:center;background:var(--magenta);color:var(--white);font-family:"Montserrat",sans-serif;font-weight:600;font-size:14px;letter-spacing:.5px;text-transform:uppercase;text-decoration:none}
.btn-line{display:flex;align-items:center;justify-content:center;border:2px solid var(--magenta);color:var(--magenta);font-family:"Montserrat",sans-serif;font-weight:600;font-size:14px;text-transform:uppercase;text-decoration:none}

/* bubbles */
.bubble{border-radius:50%;display:flex;align-items:center;justify-content:center;text-align:center;color:var(--white);font-family:"Playfair Display",serif;font-size:32px;line-height:34px}
.dot{border-radius:50%}

/* section heads */
.kicker{font-family:"Playfair Display",serif;font-size:26px;color:var(--ink)}
.title{font-family:"Playfair Display",serif;font-weight:700;font-size:44px;color:var(--teal);line-height:48px}
.sub{font-family:"Playfair Display",serif;font-size:26px;color:var(--teal)}
.para{font-family:"Raleway",sans-serif;font-weight:300;font-size:15px;line-height:24.5px;color:var(--muted)}

/* services */
.services{left:0;top:1183px;width:1200px;height:670px;background:linear-gradient(var(--grey-top) 0,var(--grey-top) 385px,var(--grey-bottom) 385px)}
.card{top:164px;width:315px;height:353px;background:var(--white);text-align:center}
.card .photo{position:absolute;left:26px;top:27px;width:263px;height:194px}
.card h3{position:absolute;left:0;width:100%;top:236px;font-family:"Playfair Display",serif;font-weight:700;font-size:18px;letter-spacing:1px;color:var(--magenta)}
.card p{position:absolute;left:30px;width:255px;top:276px;font-weight:300;font-size:14px;line-height:22px;color:var(--muted)}

/* gallery */
.gallery{left:0;top:2297px;width:1200px;height:546px;background:var(--teal-band)}
.gallery .shot{top:154px;width:243px;height:238px}
.btn-white{display:flex;align-items:center;justify-content:center;border:2px solid var(--white);color:var(--white);font-family:"Montserrat",sans-serif;font-weight:600;font-size:14px;text-transform:uppercase;text-decoration:none}

/* contact */
.info-label{font-family:"Playfair Display",serif;font-size:15px;color:var(--teal)}
.info-value{font-family:"Playfair Display",serif;font-size:20px;color:var(--ink);line-height:24px}
.info-line{display:flex;align-items:center;gap:10px;font-family:"Playfair Display",serif;font-size:20px;color:var(--ink)}

/* footer */
.footer{left:0;top:3299px;width:1200px;height:371px;background:var(--footer)}
.footer-nav{left:0;width:1200px;top:182px;display:flex;justify-content:center;gap:36px}
.footer-nav a{font-size:13px;color:#cfcfcf}
.social{left:0;width:1200px;top:248px;display:flex;justify-content:center;gap:14px}
.social span{width:14px;height:14px;border-radius:50%;background:var(--white)}
.footer-rule{left:100px;width:1000px;top:292px;height:1px;background:#555}
.copyright{left:0;width:1200px;top:324px;text-align:center;font-size:12px;color:#777}
</style>
</head>
<body>

<header>
  <div class="abs brand"><span class="brand-dot"></span><span class="brand-name">Brindle Hound</span></div>
  <nav class="abs nav">
    <a class="active" href="#">Home Page</a><a href="#">About Us</a><a href="#">Services</a><a href="#">Gallery</a><a href="#">Policies</a><a href="#">Contact Us</a>
  </nav>
</header>

<section class="abs hero" role="img" aria-label="Woman hugging a German shepherd outdoors among green foliage">
  <div class="abs hero-copy">
    <div class="big">gentle,<br>loving care</div>
    <div class="accent">for your pets</div>
    <div class="mid">in a fun &amp; friendly<br>environment</div>
  </div>
  <a class="abs btn-solid" href="#" style="left:152px;top:413px;width:180px;height:42px">Know More</a>
</section>

<section class="welcome">
  <div class="abs bubble" style="left:163px;top:857px;width:242px;height:242px;background:var(--bubble-teal)">A tired<br>pup is a<br>happy<br>pup.</div>
  <span class="abs dot" style="left:278px;top:869px;width:20px;height:20px;background:var(--bubble-pink)"></span>
  <span class="abs dot" style="left:327px;top:885px;width:25px;height:25px;background:#d6f1f4"></span>
  <span class="abs dot" style="left:355px;top:928px;width:15px;height:15px;background:var(--bubble-pink)"></span>
  <span class="abs dot" style="left:409px;top:999px;width:27px;height:27px;background:var(--bubble-teal)"></span>
  <span class="abs dot" style="left:447px;top:1026px;width:22px;height:22px;background:var(--bubble-teal)"></span>
  <span class="abs dot" style="left:145px;top:1016px;width:18px;height:18px;background:var(--bubble-pink)"></span>

  <div class="abs kicker" style="left:543px;top:818px">welcome to</div>
  <div class="abs title" style="left:543px;top:842px">Brindle Hound</div>
  <div class="abs sub" style="left:543px;top:888px">Pet Boarding &amp; Daycare!</div>
  <p class="abs para" style="left:543px;top:938px;width:535px">Brindle Hound's mission is to provide gentle, loving care for your pets in a fun and friendly environment in a way that allows you, the pet owner to worry less about your companion while you are away. We want to create a stress free environment for our furry guests and a fun, playful atmosphere for our employees.</p>
  <a class="abs btn-line" href="#" style="left:543px;top:1079px;width:137px;height:42px">Read More</a>
</section>

<section class="abs services">
  <div class="abs kicker" style="left:0;width:1200px;text-align:center;top:52px">we are trusted for our</div>
  <div class="abs title" style="left:0;width:1200px;text-align:center;top:84px">Services</div>

  <article class="abs card" style="left:100px">
    <div class="photo" role="img" aria-label="Handler playing with several dogs in a fenced yard" style="background:linear-gradient(#8a6a4e,#6b7a3e)"></div>
    <h3>DAYCARE</h3>
    <p>Socialization is an important part of raising a happy and healthy pup.</p>
  </article>
  <article class="abs card" style="left:442px">
    <div class="photo" role="img" aria-label="Fluffy cream doodle running across grass" style="background:linear-gradient(#6f5a3a,#5f7a34)"></div>
    <h3>BOARDING</h3>
    <p>Brindle Hound offers overnight boarding for dogs over 6 weeks of age.</p>
  </article>
  <article class="abs card" style="left:784px">
    <div class="photo" role="img" aria-label="Staff member greeting small white dog beside a golden retriever" style="background:linear-gradient(#8a6a4c,#7a6e44)"></div>
    <h3>GROOMING</h3>
    <p>Gentle baths, brushing and trims to keep every coat clean and tidy.</p>
  </article>

  <a class="abs btn-solid" href="#" style="left:520px;top:580px;width:161px;height:40px;letter-spacing:1.5px">Learn More</a>
</section>

<section class="policies">
  <div class="abs kicker" style="left:125px;top:1950px">safety &amp; health of your pet</div>
  <div class="abs title" style="left:125px;top:1980px">Policies</div>
  <p class="abs para" style="left:125px;top:2040px;width:500px">Brindle Hound, Inc. Pet Boarding and Daycare provides a safe, fun and stimulating social environment for dogs and puppies. To ensure the safety and health of your pet, we require all clients comply with the following rules and regulations. Safety is our Number One Priority.</p>
  <a class="abs btn-line" href="#" style="left:125px;top:2209px;width:139px;height:43px">Read More</a>

  <div class="abs bubble" style="left:747px;top:1971px;width:242px;height:242px;background:var(--bubble-pink)">Stimulating<br>and fun<br>activities</div>
  <span class="abs dot" style="left:863px;top:1983px;width:20px;height:20px;background:#b3a6d8"></span>
  <span class="abs dot" style="left:910px;top:2000px;width:27px;height:27px;background:#f1d3ea"></span>
  <span class="abs dot" style="left:942px;top:2040px;width:13px;height:13px;background:#b3a6d8"></span>
  <span class="abs dot" style="left:726px;top:2130px;width:19px;height:19px;background:var(--bubble-teal)"></span>
  <span class="abs dot" style="left:993px;top:2112px;width:28px;height:28px;background:var(--bubble-pink)"></span>
  <span class="abs dot" style="left:1030px;top:2141px;width:22px;height:22px;background:var(--bubble-pink)"></span>
</section>

<section class="abs gallery">
  <div class="abs sub" style="left:0;width:1200px;text-align:center;top:40px;color:var(--white);font-size:27px">alleviating loneliness &amp; boredom</div>
  <div class="abs title" style="left:0;width:1200px;text-align:center;top:68px;color:var(--white)">Gallery</div>
  <div class="abs shot" role="img" aria-label="Brown doodle with tongue out near a blue tunnel" style="left:100px;background:linear-gradient(#3b8fc4,#9a6a3e)"></div>
  <div class="abs shot" role="img" aria-label="Small dogs playing on grass by a wooden fence" style="left:353px;background:linear-gradient(#8a6a4c,#6f8a3a)"></div>
  <div class="abs shot" role="img" aria-label="Golden retriever and black dog in the yard" style="left:606px;background:linear-gradient(#6b6a3e,#c9a86c)"></div>
  <div class="abs shot" role="img" aria-label="Black and white dog running on grass" style="left:857px;background:linear-gradient(#8a6a4c,#6f8a3a)"></div>
  <a class="abs btn-white" href="#" style="left:529px;top:436px;width:144px;height:43px">View More</a>
</section>

<section class="contact">
  <div class="abs" role="img" aria-label="Map showing the boarding facility location" style="left:100px;top:2896px;width:449px;height:350px;background:linear-gradient(90deg,#e9ecdf 0%,#dfe8d2 60%,#a9d2f0 80%,#a9d2f0 100%)"></div>

  <div class="abs" style="left:594px;top:2921px">
    <div class="info-label">Mon - Sat</div>
    <div class="info-value">7:30am-6:00pm</div>
  </div>
  <div class="abs" style="left:594px;top:2982px">
    <div class="info-label">Sun</div>
    <div class="info-value">Boarding Pick Up/ Drop off By<br>Appointment</div>
  </div>
  <div class="abs info-line" style="left:594px;top:3088px">
    <svg width="16" height="16" viewBox="0 0 24 24"><path fill="#1cb5c4" d="M6.6 10.8a15 15 0 0 0 6.6 6.6l2.2-2.2c.3-.3.7-.4 1-.2 1.1.4 2.3.6 3.6.6.6 0 1 .4 1 1V20c0 .6-.4 1-1 1A17 17 0 0 1 3 4c0-.6.4-1 1-1h3.5c.6 0 1 .4 1 1 0 1.3.2 2.5.6 3.6.1.3 0 .7-.2 1z"/></svg>
    (555) 014-2798
  </div>
  <div class="abs info-line" style="left:594px;top:3129px">
    <svg width="16" height="12" viewBox="0 0 16 12"><rect x="0.5" y="0.5" width="15" height="11" fill="#1cb5c4"/><path d="M1 1l7 6 7-6" stroke="#fff" stroke-width="1.4" fill="none"/></svg>
    info@brindlehoundco.com
  </div>
</section>

<footer class="abs footer">
  <div class="abs dot" role="img" aria-label="Safety pledge badge" style="left:438px;top:39px;width:108px;height:108px;background:var(--teal)"></div>
  <div class="abs" role="img" aria-label="Insurance provider badge" style="left:623px;top:57px;width:169px;height:71px;background:#e2ddcf"></div>
  <nav class="abs footer-nav">
    <a class="active" href="#">Home Page</a><a href="#">About Us</a><a href="#">Services</a><a href="#">Gallery</a><a href="#">Policies</a><a href="#">Contact Us</a>
  </nav>
  <div class="abs social" aria-label="Social links"><span></span><span></span><span></span><span></span></div>
  <div class="abs footer-rule"></div>
  <div class="abs copyright">© Brindle Hound Inc. 2020 | All Right Reserved</div>
</footer>

</body>
</html>
```